依頼詳細
自転車店の看板のデザインをお願いします。
道路沿いのメイン看板になります。

店名が「PALE JUNIT」と自転車屋っぽくないのでロゴ等のデザインでパッと見て自転車屋だとわかるようにするか
CYCLESHOPと文字を入れる等、方法はお任せしますので一見でわかるようにしてください。

ロードバイクなど専門的な商品を取り扱うので清潔感や高級感があるほうが良いです。
記載項目
店名(PALE JUNIT) サイズ:縦2.46m×横1.78m
希望イメージ
シンプル 複雑
単色 カラフル
暗い 明るい
日常 高級
遊び心 厳粛
未来的 伝統的
女性的 男性的
希望する色
納品ファイル
補足説明
実際に設置する看板の写真を添付しておきます。
■ 選んだ理由

お客様や知り合いから候補を選んでいただき、その中で選定させていただきました。
他にも素敵なものはたくさんありましたが今回は看板なのでパッと見てわかる点と
年代性別問わず入りやすいデザインだと思い選ばせていただきました。

■ 提案者全員のお礼・コメント

提案していただいたランサー様、ありがとうございました。

多くのデザインを提案していただきとてもビックリしました。
今回選んだデザイン以外にもとても素敵なものがたくさんあり、
一つしか選べないことがとても残念です。

また、機会がありましたらよろしくお願いします。

```html
<!DOCTYPE html>
<html lang="en">
<head>
<meta charset="utf-8">
<title>PALE JUNIT Cycle Shop Sign</title>
<link rel="stylesheet" href="https://fonts.googleapis.com/css2?family=Roboto:wght@500;700&display=swap">
<style>
  :root {
    --stripe-light: #ffffff;
    --stripe-grey: #dcdde0;
    --sign-yellow: #f2c230;
    --sign-yellow-deep: #e3a81a;
    --navy: #1c1f5e;
    --backdrop: #eceef1;
  }
  html, body {
    margin: 0;
    padding: 0;
    width: 900px;
    height: 1200px;
    overflow: hidden;
    background: var(--backdrop);
  }
  .sign {
    position: relative;
    width: 900px;
    height: 1200px;
    background: repeating-linear-gradient(
      to bottom,
      var(--stripe-light) 0 12px,
      var(--stripe-grey) 12px 16px
    );
    overflow: hidden;
  }
  .brand {
    position: absolute;
    left: 0;
    top: 240px;
    width: 100%;
    height: 120px;
    display: flex;
    align-items: center;
    justify-content: center;
    gap: 26px;
  }
  .brand-mark {
    width: 84px;
    height: 84px;
    border-radius: 50%;
    background: var(--sign-yellow);
    flex: none;
  }
  .brand-name {
    margin: 0;
    font-family: "Roboto", sans-serif;
    font-weight: 700;
    font-size: 96px;
    line-height: 1;
    letter-spacing: 1px;
    color: var(--navy);
    white-space: nowrap;
  }
  .shop-type {
    position: absolute;
    left: 0;
    top: 530px;
    width: 100%;
    text-align: center;
    font-family: "Roboto", sans-serif;
    font-weight: 700;
    font-size: 76px;
    line-height: 1;
    letter-spacing: 2px;
    color: var(--navy);
    margin: 0;
  }
  .contact-band {
    position: absolute;
    left: 0;
    top: 620px;
    width: 900px;
    height: 580px;
  }
  .contact {
    position: absolute;
    left: 0;
    top: 790px;
    width: 100%;
    text-align: center;
    font-family: "Roboto", sans-serif;
    font-weight: 500;
    color: var(--navy);
    font-size: 58px;
    line-height: 74px;
  }
  .contact p { margin: 0; }
</style>
</head>
<body>
  <div class="sign">
    <div class="brand">
      <span class="brand-mark" aria-hidden="true"></span>
      <h1 class="brand-name">PALE JUNIT</h1>
    </div>

    <h2 class="shop-type">CYCLE SHOP</h2>

    <svg class="contact-band" viewBox="0 0 900 580" preserveAspectRatio="none" aria-hidden="true">
      <defs>
        <linearGradient id="bandFill" x1="0" y1="0" x2="0" y2="1">
          <stop offset="0" stop-color="#f2c230"/>
          <stop offset="1" stop-color="#e3a81a"/>
        </linearGradient>
      </defs>
      <path d="M0 95 C 250 70, 600 40, 900 0 L 900 580 L 0 580 Z" fill="url(#bandFill)"/>
    </svg>

    <div class="contact">
      <p>address</p>
      <p>xxx-xxxx-xxxx</p>
      <p>http://www.xxx.xxx/</p>
    </div>
  </div>
</body>
</html>
```